Website redesign and new logo

Hi we feel that the colours, layout and style along with the logo which is only text at the moment is poor. It seems to lack a quality and luxurious feel and we are about selling high end curtains. The text logo is hard to read as well in my opinion. We are looking for a overall revamp and an new logo. We want to maintain the main parts of the home page but happy to consider any ideas that will improve web traffic. It does not really reflect our achievements either of having curtains recently featured on lumen 6 tv.
The website in question is www.velmorrahangings.co.uk

```html
<!DOCTYPE html>
<html lang="en">
<head>
<meta charset="utf-8">
<title>Velmorra Hangings – Handmade Curtains</title>
<link href="https://fonts.googleapis.com/css2?family=Arimo:wght@400;700&display=swap" rel="stylesheet">
<style>
:root{
  --teal:#2e9d93;
  --teal-light:#4fb9ae;
  --teal-dark:#1f7770;
  --footer:#237e77;
  --footer-deep:#1a5f5a;
  --ink:#333;
  --muted:#666;
  --paper:#fff;
  --grey-band:#efefef;
}
*{margin:0;padding:0;box-sizing:border-box}
html,body{width:1200px;height:2471px;overflow:hidden}
body{position:relative;font-family:"Arimo",Arial,sans-serif;color:var(--ink);background:var(--paper)}
.abs{position:absolute}

/* hero */
.hero-photo{left:0;top:0;width:1200px;height:830px;
  background:linear-gradient(180deg,#2f5a55 0%,#5c8d84 30%,#7ea59b 55%,#c9cbb9 75%,#dcd8c8 100%);}
.hero-photo::before{content:"";position:absolute;left:0;top:0;width:240px;height:700px;
  background:linear-gradient(90deg,#c9b423,#e9d64a 60%,#b9a21c)}
.hero-photo::after{content:"";position:absolute;right:0;top:0;width:180px;height:520px;
  background:linear-gradient(90deg,#dfe9e4,#f2f2ea)}
.brand{left:480px;top:0;width:220px;height:115px;background:var(--teal);
  display:flex;align-items:center;justify-content:center;box-shadow:0 4px 10px rgba(0,0,0,.3)}
.brand-name{color:#fff;font-size:30px;font-weight:400;letter-spacing:1px}
.top-contact{left:808px;top:44px;color:#fff;font-size:14px;line-height:19px}
.top-contact strong{font-size:16px}
.main-nav{left:156px;top:124px;width:850px;display:flex;gap:22px;border-bottom:1px solid rgba(255,255,255,.5);padding-bottom:8px}
.main-nav a{color:#fff;text-decoration:none;font-size:14px;text-transform:uppercase;letter-spacing:.3px}
.main-nav a.current{font-weight:700}
.promo{left:261px;top:292px;width:673px;height:50px;background:var(--teal);
  color:#fff;font-weight:700;font-size:34px;text-align:center;line-height:50px}
.promo-sub{left:261px;top:346px;width:673px;text-align:center;color:#fff;font-weight:700;font-size:27px;text-shadow:0 1px 3px rgba(0,0,0,.4)}

/* feature cards */
.card{background:linear-gradient(180deg,var(--teal-light),var(--teal) 40%,var(--teal-dark));
  color:#fff;text-align:center;box-shadow:0 12px 18px rgba(0,0,0,.3)}
.card h3{font-weight:400;font-size:17px;line-height:21px;padding:22px 18px 0}
.card .thumb{margin:14px auto 0;width:232px;height:118px}
.card p{font-size:12px;line-height:16px;padding:14px 24px 0}
.card-fabric{left:151px;top:590px;width:283px;height:289px}
.card-review{left:448px;top:549px;width:293px;height:371px}
.card-news{left:760px;top:590px;width:292px;height:289px}
.card-review .thumb{height:120px;width:234px}
.card-review .reviewer{font-weight:700;font-size:13px;padding-top:14px}

/* intro */
.section-title{font-weight:400;font-size:26px;color:#222}
.intro-title{left:151px;top:1005px}
.intro-copy{left:151px;top:1050px;width:450px;font-size:14.5px;line-height:19px;color:var(--muted)}
.intro-copy p{margin-bottom:19px}
.designer-title{left:654px;top:1005px}
.video{left:654px;top:1057px;width:370px;height:247px;background:linear-gradient(135deg,#3a2a1e,#d9cdb8 45%,#5a3f2a 70%,#e8e2d6);box-shadow:0 2px 6px rgba(0,0,0,.3)}
.video-bar{left:0;bottom:0;width:100%;height:26px;background:rgba(20,20,20,.85)}

/* areas */
.areas-band{left:0;top:1373px;width:1200px;height:426px;background:var(--grey-band);
  box-shadow:inset 0 10px 14px -8px rgba(0,0,0,.15)}
.areas-title{left:0;top:1470px;width:1200px;text-align:center;font-size:25px;color:#222}
.area{width:130px;text-align:center;font-size:13px;line-height:19px;color:#444}
.area .disc{width:110px;height:110px;border-radius:50%;margin:0 auto 12px;background:var(--teal);
  border:5px solid #bfe0dc;display:flex;align-items:center;justify-content:center}

/* gallery */
.gallery{left:0;top:1799px;width:1200px;height:398px;background:linear-gradient(180deg,#36a197,var(--teal))}
.gallery-title{left:0;top:1858px;width:1200px;text-align:center;color:#fff;font-size:25px}
.gallery-item{top:1928px;height:200px;box-shadow:0 10px 14px rgba(0,0,0,.35)}

/* footer */
.footer{left:0;top:2197px;width:1200px;height:186px;background:var(--footer)}
.footer-brand{left:96px;top:2230px;width:214px;height:118px;background:var(--teal);
  display:flex;align-items:center;justify-content:center;box-shadow:0 3px 8px rgba(0,0,0,.25)}
.footer-contact{left:790px;top:2232px;color:#fff;font-size:14px;line-height:19px}
.contact-row{display:flex;gap:14px;align-items:flex-start;margin-bottom:10px}
.contact-row svg{flex:none}
.legal-bar{left:0;top:2383px;width:1200px;height:88px;background:var(--footer-deep)}
.legal{left:156px;top:2410px;color:#fff;font-size:10px;line-height:14px;text-transform:uppercase}
.social{left:783px;top:2408px;display:flex;gap:14px}
.social span{width:16px;height:16px;border-radius:50%;background:#fff;opacity:.9}
</style>
</head>
<body>

<!-- hero -->
<div class="abs hero-photo" role="img" aria-label="Living room with yellow patterned curtains, teal damask wallpaper, white sofa and lamp"></div>
<div class="abs brand"><span class="brand-name">Velmorra</span></div>
<div class="abs top-contact"><strong>0300 555 0199</strong><br>info@velmorrahangings.co.uk</div>
<nav class="abs main-nav">
  <a class="current" href="#">Home</a><a href="#">About us</a><a href="#">News</a><a href="#">Fabrics</a>
  <a href="#">Scatter cushions &amp; bed throws</a><a href="#">Gallery</a><a href="#">Testimonials</a><a href="#">Contact us</a>
</nav>
<div class="abs promo">Double Your House for half the money</div>
<div class="abs promo-sub">See Our Curtains on lumen 6</div>

<div class="abs card card-fabric">
  <h3>Curtain Fabric types<br>include</h3>
  <div class="thumb" role="img" aria-label="Cream curtains in a bright room" style="background:linear-gradient(135deg,#8a7a5c,#e9dfc6 50%,#a68f68)"></div>
  <p>An expert in home measuring<br>service and professional hanging.</p>
</div>
<div class="abs card card-review">
  <h3>Our Customers<br>love us</h3>
  <div class="thumb" role="img" aria-label="Portrait of a happy customer" style="background:linear-gradient(135deg,#cfcfcf,#ece6e0 50%,#b5a495)"></div>
  <div class="reviewer">Mrs H, Reading</div>
  <p>The room is so much brighter now,<br>and I love the contrasting cushions.<br><br>Thank you for your advice.</p>
</div>
<div class="abs card card-news">
  <h3>Our Latest Curtain<br>and Fabric News</h3>
  <div class="thumb" role="img" aria-label="White sheer curtains beside green plants" style="background:linear-gradient(135deg,#4f6e3a,#dfe6dc 55%,#f4f4f0)"></div>
  <p>We provide a made to measure<br>curtain service</p>
</div>

<!-- intro -->
<h2 class="abs section-title intro-title">Handmade Curtains</h2>
<div class="abs intro-copy">
  <p>One of the many advantages of handmade curtains or made to measure curtains is that they fit perfectly and compliment the room. Often curtains that are purchased already-made do not fit as they should and the end results reflect this.</p>
  <p>With handmade curtains or made to measure curtains obviously the style can be exactly as you choose with a wide range of different headers and linings available. Handmade curtains although more expensive than made to measure curtains have the advantage of no visible machine stitching.</p>
  <p>We carry sample handmade curtains and also made to measure curtains so you can study and see how they are manufactured. We have a extensive range of fabric from which our handmade curtains or made measure curtains can be produced from.</p>
</div>
<h2 class="abs section-title designer-title">Meet Verity designer</h2>
<div class="abs video" role="img" aria-label="Video still of patterned curtains at a window">
  <svg class="abs" style="left:155px;top:100px" width="60" height="42" viewBox="0 0 60 42"><rect width="60" height="42" rx="8" fill="#1b1b1b" opacity=".85"/><path d="M24 12 L40 21 L24 30 Z" fill="#fff"/></svg>
  <div class="abs video-bar">
    <svg class="abs" style="left:10px;top:7px" width="12" height="12" viewBox="0 0 12 12"><path d="M1 0 L11 6 L1 12 Z" fill="#fff"/></svg>
    <span class="abs" style="left:56px;top:6px;color:#ddd;font-size:11px">0:00 / 6:07</span>
  </div>
</div>

<!-- areas -->
<div class="abs areas-band"></div>
<h2 class="abs areas-title" style="font-weight:400">The areas we cover include</h2>
<div class="abs area" style="left:193px;top:1532px"><div class="disc"></div>Curtains<br>Berkshire</div>
<div class="abs area" style="left:319px;top:1532px"><div class="disc"></div>Curtains<br>Buckinghamshire</div>
<div class="abs area" style="left:451px;top:1532px"><div class="disc" style="background:var(--teal-dark)"></div>Curtains<br>Oxfordshire</div>
<div class="abs area" style="left:586px;top:1532px"><div class="disc"></div>Curtains<br>Winchester</div>
<div class="abs area" style="left:712px;top:1532px"><div class="disc" style="background:var(--teal-dark)"></div>Curtains<br>Guildford</div>
<div class="abs area" style="left:841px;top:1532px"><div class="disc"></div>Curtains<br>Oxford</div>

<!-- gallery -->
<div class="abs gallery"></div>
<h2 class="abs gallery-title" style="font-weight:400">Our Curtains Gallery</h2>
<div class="abs gallery-item" style="left:60px;width:253px;background:linear-gradient(135deg,#6b5a3a,#e7e1cf 55%,#8c7a56)" role="img" aria-label="Lounge with patterned curtains and armchair"></div>
<div class="abs gallery-item" style="left:335px;width:255px;background:linear-gradient(135deg,#5a4326,#c9a873 50%,#6e5230)" role="img" aria-label="Dining room with gold curtains"></div>
<div class="abs gallery-item" style="left:612px;width:256px;background:linear-gradient(135deg,#c9c3b6,#f0ece4 50%,#8b7456)" role="img" aria-label="Living room with sofas and tall windows"></div>
<div class="abs gallery-item" style="left:890px;width:255px;background:linear-gradient(135deg,#6a5a48,#d8cbb4 50%,#9a8062)" role="img" aria-label="Bay window with cream curtains and sofa"></div>

<!-- footer -->
<footer>
<div class="abs footer"></div>
<div class="abs footer-brand"><span class="brand-name">Velmorra</span></div>
<div class="abs footer-contact">
  <div class="contact-row">
    <svg width="18" height="26" viewBox="0 0 18 26"><path d="M9 0a9 9 0 0 1 9 9c0 7-9 17-9 17S0 16 0 9a9 9 0 0 1 9-9z" fill="#fff"/><circle cx="9" cy="9" r="3.5" fill="var(--footer)"/></svg>
    <div>Velmorra Hangings,<br>12 Riverside Row, Ashbourne,<br>Berkshire, RG9 4ZX</div>
  </div>
  <div class="contact-row">
    <svg width="20" height="20" viewBox="0 0 20 20"><circle cx="10" cy="10" r="9" fill="none" stroke="#fff" stroke-width="1.6"/><path d="M6.5 5.5l2 2-1 1.5c.7 1.5 1.8 2.6 3.3 3.3l1.5-1 2 2-1.3 1.4c-3.5-.5-6.4-3.4-6.9-6.9z" fill="#fff"/></svg>
    <div>0300 555 0199</div>
  </div>
  <div class="contact-row">
    <svg width="20" height="20" viewBox="0 0 20 20"><circle cx="10" cy="10" r="9" fill="none" stroke="#fff" stroke-width="1.6"/><rect x="5" y="6.5" width="10" height="7" fill="none" stroke="#fff" stroke-width="1.2"/><path d="M5 6.5l5 4 5-4" fill="none" stroke="#fff" stroke-width="1.2"/></svg>
    <div>info@velmorrahangings.co.uk</div>
  </div>
</div>
<div class="abs legal-bar"></div>
<div class="abs legal">All rights reserved © Velmorra Hangings<br>Terms of use · Privacy policies · Cookies</div>
<div class="abs social"><span></span><span></span><span></span><span></span><span></span><span></span></div>
</footer>

</body>
</html>
```